Business card design and logo for plumbing bussiness

We are wanting a logo for a plumbing business is Queensland Australia. KRV Plumbing and Drainage will be doing works on domestic and commercial sites.
Plumbing, drainage and gas works. We are wanting something that will stand out and be noticed. Colours could be black blue and white but open for suggestions.

Target Market(s)

Builders and home renovators

Industry/Entity Type

Plumbing

Contact Information for Business Card

Miles Dorgan - Director
0417 582 913
miles@krvplumbing.example.com.au
QBCC: 847 2106
ABN: 52 319 407 281

Font styles to use
Sans Serif

Colors
000000

Requirements
Must have
• Clear defined branding

```html
<!DOCTYPE html>
<html lang="en">
<head>
<meta charset="utf-8">
<title>KRV Plumbing and Drainage – Business Card</title>
<link rel="stylesheet" href="https://fonts.googleapis.com/css2?family=Oswald:wght@700&family=Arimo:wght@400&display=swap">
<style>
  :root {
    --page: #ffffff;
    --card: #141414;
    --blue: #0a6fe8;
    --blue-deep: #0d4fa8;
    --white: #ffffff;
    --photo-light: #8a8a8a;
    --photo-dark: #3a3a3a;
  }
  * { margin: 0; padding: 0; box-sizing: border-box; }
  html, body {
    width: 1200px; height: 864px; overflow: hidden;
    background: var(--page);
  }
  .canvas { position: relative; width: 1200px; height: 864px; }
  .card {
    position: absolute;
    left: 297px;
    width: 607px;
    height: 347px;
    background: var(--card);
    overflow: hidden;
  }
  .card--front { top: 64px; }
  .card--back { top: 454px; }

  .front-art { position: absolute; inset: 0; }

  .name {
    position: absolute; left: 36px; top: 60px;
    font-family: "Oswald", "Arial Narrow", sans-serif;
    font-weight: 700; font-size: 43px; line-height: 1;
    color: var(--white); letter-spacing: 0;
    text-transform: uppercase;
  }
  .role {
    position: absolute; left: 37px; top: 108px;
    font-family: "Arimo", Arial, sans-serif;
    font-size: 20px; letter-spacing: 1px;
    color: var(--blue); text-transform: uppercase;
  }
  .contacts {
    position: absolute; left: 36px; top: 180px;
    list-style: none;
    font-family: "Arimo", Arial, sans-serif;
    font-size: 21px; color: var(--white);
  }
  .contacts li {
    display: flex; align-items: center; gap: 10px;
    height: 29px;
  }
  .contacts svg { width: 20px; height: 20px; flex: none; }
  .contacts .email { text-transform: uppercase; font-size: 17px; }
  .hash {
    width: 20px; text-align: center;
    color: var(--blue); font-size: 24px; flex: none;
  }

  .brand {
    position: absolute;
    display: flex; align-items: center;
    font-family: "Arimo", Arial, sans-serif;
    color: var(--white); white-space: nowrap;
  }
  .brand__dot { border-radius: 50%; background: var(--blue-deep); flex: none; }
  .brand--front { left: 360px; top: 296px; font-size: 15px; gap: 7px; }
  .brand--front .brand__dot { width: 26px; height: 26px; }
  .brand--back { right: 22px; top: 268px; font-size: 25px; gap: 10px; }
  .brand--back .brand__dot { width: 50px; height: 50px; }
</style>
</head>
<body>
<main class="canvas">

  <section class="card card--front" aria-label="Business card front">
    <svg class="front-art" viewBox="0 0 607 347" width="607" height="347">
      <defs>
        <linearGradient id="pipesTone" x1="0" y1="0" x2="1" y2="1">
          <stop offset="0" stop-color="var(--photo-light)"/>
          <stop offset="0.6" stop-color="var(--photo-dark)"/>
          <stop offset="1" stop-color="#6c6c6c"/>
        </linearGradient>
      </defs>
      <polygon class="photo-area" role="img"
        aria-label="Black and white photograph of old cast-iron drain pipes on a brick wall"
        points="348,0 607,0 607,347 560,347" fill="url(#pipesTone)"/>
      <polygon class="accent-stripe" points="316,0 348,0 560,347 530,347" fill="var(--blue)"/>
    </svg>

    <h1 class="name">Miles Dorgan</h1>
    <p class="role">Director</p>

    <ul class="contacts">
      <li>
        <svg viewBox="0 0 20 20" aria-hidden="true">
          <circle cx="10" cy="10" r="8.6" fill="none" stroke="var(--blue)" stroke-width="1.6"/>
          <path d="M7.2 5.6c.5-.3 1-.2 1.3.3l.8 1.5c.2.4.1.9-.3 1.2l-.5.4c.4 1 1.3 2 2.3 2.4l.4-.5c.3-.4.8-.5 1.2-.3l1.5.8c.5.3.6.8.3 1.3-.6.9-1.5 1.3-2.5 1-2.3-.8-4.1-2.6-4.9-4.9-.3-1 .1-2 .9-2.5z" fill="var(--blue)"/>
        </svg>
        <span>0417 582 913</span>
      </li>
      <li>
        <svg viewBox="0 0 20 20" aria-hidden="true">
          <circle cx="10" cy="10" r="9.5" fill="var(--blue)"/>
          <rect x="5.3" y="6.6" width="9.4" height="6.8" rx="0.8" fill="none" stroke="var(--card)" stroke-width="1.3"/>
          <path d="M5.6 7.2 10 10.4l4.4-3.2" fill="none" stroke="var(--card)" stroke-width="1.3"/>
        </svg>
        <span class="email">miles@krvplumbing.example.com.au</span>
      </li>
      <li><span class="hash">#</span><span>QBCC: 847 2106</span></li>
      <li><span class="hash">#</span><span>ABN: 52 319 407 281</span></li>
    </ul>

    <div class="brand brand--front">
      <span class="brand__dot" aria-hidden="true"></span>
      <span class="brand__name">KRV Plumbing</span>
    </div>
  </section>

  <section class="card card--back" aria-label="Business card back">
    <div class="brand brand--back">
      <span class="brand__dot" aria-hidden="true"></span>
      <span class="brand__name">KRV Plumbing</span>
    </div>
  </section>

</main>
</body>
</html>
```